Multi App design - layout and graphic suggestions to our new app

Update:
Making a modern and futuristic design of a multifunctional app.
Attached is a description of some of the functionalities.
We need this innovative elegant design on buttons, menu, screens and other elements to be applied onto several mobile screens to choose a style that can be chosen.
Future apps will even include robot assistance, new navigation logic and 3Dish style and several templates to variate the style (look and feel).
Looking forward to see some really new style of futuristic apps!
(We like the app vrolp.com - although our design shall be even more modern and creative)

Multi-function app

We would like to have a design suggestion for a multi-function app.

The design shall show front end design as well as navigation and UI/UX user interface

It’s and generic shopping app enabling a long list of services where end user get a menu which is graphical and can be extended with new services as well as customized by end user.
Each service contains functionality as well as content and findings.
Among 5-10 initial services are:

• Shopping assistant and Travel assistant – finding relevant shops/museum and products nearby – sorted by Geofence and Beacons for presenting information - or find stores and experiences
• Loyalty points / Contests and bonus points - preferences and sharing reviews 
• QR and Barcode reader – for increased information
• Campaigns
• Support and feedback

Flexible application - with simple possibility to add new services and allow the user to control the order of the menu / own top menu
Simpler social sharing - reviews, feedback, loyalty points across shops etc.
Easy user management - turn off shops or functionality - without uninstalling

Target Market(s)

End user

Industry/Entity Type

Inn

Requirements
Must have
• The design shall show front end design as well as navigation and UI/UX user interface.
• Attached is your logo and colors with codes

```html
<!DOCTYPE html>
<html lang="en">
<head>
<meta charset="utf-8">
<title>Best for Coffee</title>
<link rel="stylesheet" href="https://fonts.googleapis.com/css2?family=Lato:wght@300;400;700&display=swap">
<style>
  :root {
    --teal: #0b9299;
    --teal-badge: #0d9aa0;
    --page: #f2f2f2;
    --ink: #3a3a3a;
    --muted: #7c7c7c;
    --tab-ink: #222222;
    --white: #ffffff;
  }
  * { box-sizing: border-box; margin: 0; padding: 0; }
  html, body { width: 675px; height: 1200px; overflow: hidden; }
  body { font-family: "Lato", sans-serif; background: var(--page); position: relative; }

  .status-bar {
    position: absolute; top: 0; left: 0; width: 675px; height: 36px;
    background: var(--teal); color: var(--white); font-size: 19px;
    display: flex; align-items: center; justify-content: space-between; padding: 0 10px;
  }
  .status-bar .carrier { display: flex; align-items: center; gap: 6px; }
  .status-bar .time { position: absolute; left: 0; right: 0; text-align: center; pointer-events: none; }
  .status-bar .battery { display: flex; align-items: center; gap: 6px; }

  .nav-bar {
    position: absolute; top: 36px; left: 0; width: 675px; height: 79px;
    background: var(--teal); color: var(--white);
  }
  .nav-bar .title {
    position: absolute; left: 0; right: 0; top: 20px; text-align: center;
    font-weight: 700; font-size: 29px; letter-spacing: 0.2px;
  }
  .nav-bar .back { position: absolute; left: 34px; top: 22px; }
  .nav-bar .share { position: absolute; right: 34px; top: 20px; }

  .hero {
    position: absolute; top: 115px; left: 0; width: 675px; height: 425px;
    background: linear-gradient(180deg, #1f3340 0%, #24323a 40%, #2d2623 70%, #3b2c25 100%);
    color: var(--white); text-align: center;
  }
  .hero .headline {
    position: absolute; top: 157px; left: 60px; right: 60px;
    font-size: 28px; line-height: 38px; font-weight: 400;
  }
  .hero .byline { position: absolute; top: 250px; left: 0; right: 0; font-size: 19px; font-weight: 300; }
  .hero .curator {
    position: absolute; top: 400px; left: 0; right: 0; top: 400px;
  }
  .curator-row {
    position: absolute; top: 285px; left: 0; right: 0;
    display: flex; justify-content: center; align-items: center; gap: 12px;
    font-weight: 700; font-size: 20px;
  }
  .avatar { width: 36px; height: 36px; border-radius: 50%; background: linear-gradient(135deg, #7a3b26, #d17a3d); }

  .places {
    position: absolute; top: 576px; left: 36px; width: 603px;
    display: grid; grid-template-columns: repeat(3, 180px); column-gap: 32px; row-gap: 0;
  }
  .place { height: 335px; }
  .place .photo { position: relative; width: 180px; height: 180px; }
  .photo.cafe { background: linear-gradient(160deg, #c0703c, #5a3522 60%, #2a2020); }
  .photo.plate { background: radial-gradient(circle at 50% 55%, #6b4a36 0%, #3a2c26 45%, #1f2226 100%); }
  .photo.pasta { background: radial-gradient(circle at 55% 55%, #c9a83a 0%, #6f7d2e 40%, #d8d8d6 72%, #3a3a3c 100%); }
  .rating {
    position: absolute; top: 8px; left: 9px; width: 45px; height: 34px;
    background: var(--teal-badge); color: var(--white); font-size: 22px;
    display: flex; align-items: center; justify-content: center;
  }
  .place .name { margin-top: 20px; font-size: 24px; line-height: 31px; color: var(--ink); }
  .place .area { margin-top: 6px; font-size: 20px; color: var(--muted); font-weight: 400; }

  .tab-bar {
    position: absolute; top: 1112px; left: 0; width: 675px; height: 88px;
    background: var(--white); display: flex; justify-content: space-between;
    padding: 0 12px; border-top: 1px solid #ececec;
  }
  .tab { width: 130px; display: flex; flex-direction: column; align-items: center; padding-top: 14px; }
  .tab .label { margin-top: 6px; font-size: 20px; color: var(--muted); }
  .tab.active .label { color: var(--muted); }
</style>
</head>
<body>
  <div class="status-bar">
    <div class="carrier">
      <span>●●●●●</span><span>Relay</span>
      <svg width="20" height="15" viewBox="0 0 20 15"><path d="M1 5 Q10 -2 19 5 L17 7 Q10 1 3 7Z M5 9 Q10 5 15 9 L13 11 Q10 8.5 7 11Z M10 15 L8 13 Q10 11.5 12 13Z" fill="#fff"/></svg>
    </div>
    <div class="time">9:41 AM</div>
    <div class="battery">
      <span>100%</span>
      <svg width="40" height="18" viewBox="0 0 40 18"><rect x="1" y="1" width="34" height="16" rx="3" fill="none" stroke="#fff" stroke-width="1.5"/><rect x="3" y="3" width="30" height="12" rx="1.5" fill="#fff"/><rect x="36.5" y="6" width="2.5" height="6" rx="1" fill="#fff"/></svg>
    </div>
  </div>

  <header class="nav-bar">
    <svg class="back" width="18" height="32" viewBox="0 0 18 32"><path d="M15 3 L3 16 L15 29" fill="none" stroke="#fff" stroke-width="2.5"/></svg>
    <h1 class="title">BEST FOR COFFEE</h1>
    <svg class="share" width="30" height="38" viewBox="0 0 30 38"><path d="M10 12 H2 V36 H28 V12 H20" fill="none" stroke="#fff" stroke-width="1.6"/><path d="M15 24 V2 M9 8 L15 2 L21 8" fill="none" stroke="#fff" stroke-width="1.6"/></svg>
  </header>

  <section class="hero" role="img" aria-label="Blurred photo of a cosy cafe interior with pendant lamps and potted plants">
    <p class="headline">Spend a good time with high quality cofee in calming places</p>
    <p class="byline">Collection by</p>
    <div class="curator-row"><span class="avatar" role="img" aria-label="Curator avatar"></span><span>Mira Tolven</span></div>
  </section>

  <main class="places">
    <article class="place">
      <div class="photo cafe" role="img" aria-label="Cafe storefront with guests seated at the window"><span class="rating">4.2</span></div>
      <h2 class="name">Amber Crumb</h2>
      <p class="area">Brygga, Vestby</p>
    </article>
    <article class="place">
      <div class="photo plate" role="img" aria-label="Plated dessert with berries on a wooden board"><span class="rating">4.2</span></div>
      <h2 class="name">Lindholm Cafe &amp; Bistro</h2>
      <p class="area">Torvgata, Vestby</p>
    </article>
    <article class="place">
      <div class="photo pasta" role="img" aria-label="Bowl of spaghetti with spinach and cheese"><span class="rating">4.2</span></div>
      <h2 class="name">Verne Restauration</h2>
      <p class="area">Torvgata, Vestby</p>
    </article>
    <article class="place">
      <div class="photo cafe" role="img" aria-label="Cafe storefront with guests seated at the window"><span class="rating">4.2</span></div>
    </article>
    <article class="place">
      <div class="photo plate" role="img" aria-label="Plated dessert with berries on a wooden board"><span class="rating">4.2</span></div>
    </article>
    <article class="place">
      <div class="photo pasta" role="img" aria-label="Bowl of spaghetti with spinach and cheese"><span class="rating">4.2</span></div>
    </article>
  </main>

  <nav class="tab-bar">
    <div class="tab active">
      <svg width="40" height="34" viewBox="0 0 40 34"><path d="M2 6 L13 2 L27 6 L38 2 V28 L27 32 L13 28 L2 32Z M13 2 V28 M27 6 V32" fill="none" stroke="#0b9299" stroke-width="2.2" stroke-linejoin="round"/></svg>
      <span class="label">Places</span>
    </div>
    <div class="tab">
      <svg width="36" height="34" viewBox="0 0 36 34"><path d="M2 10 V2 H10 M26 2 H34 V10 M34 24 V32 H26 M10 32 H2 V24" fill="none" stroke="#222" stroke-width="3"/></svg>
      <span class="label">Scan</span>
    </div>
    <div class="tab">
      <svg width="34" height="40" viewBox="0 0 34 40"><path d="M9 22 L3 36 L10 34 L13 40 L17 28 L21 40 L24 34 L31 36 L25 22Z" fill="#222"/><circle cx="17" cy="14" r="13" fill="#222"/><circle cx="17" cy="14" r="8" fill="none" stroke="#fff" stroke-width="2"/></svg>
      <span class="label">Point</span>
    </div>
    <div class="tab">
      <svg width="36" height="36" viewBox="0 0 36 36"><circle cx="18" cy="10" r="9" fill="#222"/><path d="M1 36 Q1 21 18 21 Q35 21 35 36Z" fill="#222"/></svg>
      <span class="label">Profile</span>
    </div>
  </nav>
</body>
</html>
```